Stationery Design Project

KT7 Staffing requires letterhead and business card designs for a company based in London. Just like the name, we're a management resourcing company, providing resources to third party companies. You can see www.kt7staffing-example.com for ideas on existing colour schemes and design concepts that have been implimented and agreed to. Ultimately the design should broadcast professionalism, safety and the concept of growth.

Target Market(s)

Financial institutes; friendly societies (All UK based)

Industry/Entity Type

Safety

Requirements
Must have
• Files produced should be print ready; and the text in them editable (eg address, name etc)

```html
<!DOCTYPE html>
<html lang="en">
<head>
<meta charset="utf-8">
<title>KT7 Staffing — Business Card</title>
<link rel="stylesheet" href="https://fonts.googleapis.com/css2?family=Arimo:wght@400;700&display=swap">
<style>
  :root {
    --teal: #2cc09c;
    --aqua: #7fe0ea;
    --ink: #4a4a4a;
    --edge: #2b2b2b;
    --paper: #ffffff;
  }
  * { margin: 0; padding: 0; box-sizing: border-box; }
  html, body {
    width: 981px; height: 1200px; overflow: hidden;
    background: var(--paper);
    font-family: "Arimo", Arial, sans-serif;
  }
  .sheet { position: relative; width: 981px; height: 1200px; }
  .card {
    position: absolute; left: 2px; width: 977px;
    border: 2px solid var(--edge); background: var(--paper);
  }
  .card--front { top: 2px; height: 556px; }
  .card--back { top: 637px; height: 561px; }

  .brand-dot { position: absolute; border-radius: 50%; background: var(--teal); }
  .brand-rule { position: absolute; width: 3px; background: var(--aqua); }

  .card--front .brand-dot { left: 124px; top: 222px; width: 106px; height: 106px; }
  .card--front .brand-rule { left: 254px; top: 200px; height: 153px; }
  .brand-name {
    position: absolute; left: 280px; top: 222px;
    font-weight: 700; font-size: 94px; line-height: 1;
    color: var(--teal); letter-spacing: -1px; white-space: nowrap;
  }

  .card--back .brand-dot { left: 96px; top: 128px; width: 100px; height: 100px; }
  .card--back .brand-rule { left: 217px; top: 118px; height: 131px; }

  .contact { position: absolute; left: 310px; top: 116px; color: var(--ink); }
  .contact__name {
    font-weight: 700; font-size: 49px; line-height: 1;
    color: var(--teal); letter-spacing: 0.5px;
  }
  .contact__role {
    margin-top: 8px; font-size: 31px; line-height: 1;
    color: var(--aqua); letter-spacing: 0.3px;
  }
  .contact__email { margin-top: 24px; font-size: 27px; line-height: 1; }
  .contact__phones { margin-top: 30px; font-size: 27px; line-height: 35px; }
  .contact__address { margin-top: 37px; font-size: 27px; line-height: 1; white-space: nowrap; }
  .contact__web {
    margin-top: 14px; font-weight: 700; font-size: 32px; line-height: 1;
    color: var(--teal);
  }
</style>
</head>
<body>
<main class="sheet">
  <section class="card card--front" aria-label="Business card front">
    <span class="brand-dot"></span>
    <span class="brand-rule"></span>
    <div class="brand-name">KT7 Staffing</div>
  </section>

  <section class="card card--back" aria-label="Business card back">
    <span class="brand-dot"></span>
    <span class="brand-rule"></span>
    <div class="contact">
      <h1 class="contact__name">DANIEL HARTLEY</h1>
      <p class="contact__role">CHIEF FINANCIAL OFFICER</p>
      <p class="contact__email">dhartley@kt7staffing-example.com</p>
      <p class="contact__phones">
        Tel: 020.555.0148 ext. 317<br>
        Cell: 07700.555.264<br>
        Fax: 020-555-0190
      </p>
      <p class="contact__address">18 Fenwick Row, Suite 4C &nbsp;|&nbsp; London EC2A 4BX</p>
      <p class="contact__web">www.kt7staffing-example.com</p>
    </div>
  </section>
</main>
</body>
</html>
```